Derya & Kerem Wedding Invitation and Decorative Designs

We are looking for a sweet and elegant design for our wedding invitation. We need different versions of the same design to use both as printed hard copies and in digital formats (WhatsApp image, instagram post, etc) Please see attached sample invitation, which we like as a simple and elegant option, but also find it quite basic. We are open to creative suggestions following a similar style.
Once we decide on an invitation design, we would like to use the same design elements in guest name cards, welcome sign, menu cards and print cover for the dance floor of our wedding venue. Please see random samples of these materials attached. We also attach a photo from our wedding venue displaying a close to final visual of the decoration we chose for our wedding day (sharing in case it helps as an inspiration source and helps with matching decoration colors with the designs)
Requirements
Must have
- Must have a style similar to the attached sample invitation

```html
<!DOCTYPE html>
<html lang="tr">
<head>
<meta charset="utf-8">
<title>Derya &amp; Kerem – Davetiye</title>
<link rel="stylesheet" href="https://fonts.googleapis.com/css2?family=Great+Vibes&family=Parisienne&family=Old+Standard+TT:wght@400&display=swap">
<style>
  :root {
    --backdrop: #000000;
    --card-light: #fbfbfb;
    --card-fold: #e7e7e9;
    --accent-red: #a83a36;
    --floral-soft: #efd6d3;
    --ink: #141414;
  }
  * { margin: 0; padding: 0; box-sizing: border-box; }
  html, body { width: 1200px; height: 873px; overflow: hidden; background: var(--backdrop); }
  .canvas { position: relative; width: 1200px; height: 873px; background: var(--backdrop); }

  .card {
    position: absolute;
    overflow: hidden;
    background:
      radial-gradient(ellipse at 30% 25%, var(--card-light) 0%, transparent 55%),
      radial-gradient(ellipse at 70% 70%, var(--card-light) 0%, transparent 60%),
      linear-gradient(160deg, var(--card-fold) 0%, var(--card-light) 35%, var(--card-fold) 60%, var(--card-light) 100%);
  }
  .floral {
    position: absolute;
    background: radial-gradient(ellipse at center, var(--floral-soft) 0%, rgba(239,214,211,0.35) 60%, transparent 100%);
  }

  .couple-name {
    position: absolute;
    font-family: "Great Vibes", cursive;
    color: var(--accent-red);
    line-height: 1;
    white-space: nowrap;
  }

  /* Front card */
  .card--front { left: 124px; top: 392px; width: 458px; height: 315px; }
  .card--front .floral--top { right: 0; top: 0; width: 100px; height: 105px; }
  .card--front .floral--bottom { left: 36px; bottom: 0; width: 95px; height: 105px; }
  .card--front .name-first { left: 102px; top: 110px; font-size: 60px; }
  .card--front .name-second { left: 200px; top: 158px; font-size: 60px; }

  /* Details card */
  .card--details { left: 640px; top: 114px; width: 458px; height: 645px; }
  .card--details .floral--top { right: 0; top: 0; width: 110px; height: 146px; }
  .card--details .floral--bottom { left: 0; bottom: 0; width: 102px; height: 178px; }
  .card--details .name-first { left: 104px; top: 58px; font-size: 58px; }
  .card--details .name-second { left: 196px; top: 102px; font-size: 58px; }

  .message {
    position: absolute; left: 0; right: 0; top: 176px;
    text-align: center;
    font-family: "Parisienne", cursive;
    font-size: 19px; line-height: 32px;
    color: var(--ink);
  }
  .invited {
    position: absolute; left: 0; right: 0; top: 372px;
    text-align: center;
    font-family: "Old Standard TT", serif;
    font-size: 27px; color: var(--accent-red);
  }
  .venue {
    position: absolute; left: 0; right: 0; top: 440px;
    text-align: center;
    font-family: "Old Standard TT", serif;
    font-size: 17px; line-height: 26.5px; color: var(--ink);
    font-style: normal;
  }
  .event-date {
    position: absolute; left: 0; right: 0; top: 566px;
    text-align: center;
    font-family: "Old Standard TT", serif;
    font-size: 16px; color: var(--ink);
  }
</style>
</head>
<body>
<main class="canvas">

  <section class="card card--front" aria-label="Davetiye ön yüz">
    <div class="floral floral--top" role="img" aria-label="Kırmızı çizgili çiçek illüstrasyonu"></div>
    <div class="floral floral--bottom" role="img" aria-label="Kırmızı çizgili çiçek illüstrasyonu"></div>
    <h1 class="couple-name name-first">Derya&amp;</h1>
    <p class="couple-name name-second">Kerem</p>
  </section>

  <section class="card card--details" aria-label="Davetiye detayları">
    <div class="floral floral--top" role="img" aria-label="Kırmızı çizgili çiçek illüstrasyonu"></div>
    <div class="floral floral--bottom" role="img" aria-label="Kırmızı çizgili çiçek illüstrasyonu"></div>
    <h2 class="couple-name name-first">Derya&amp;</h2>
    <p class="couple-name name-second">Kerem</p>

    <p class="message">Bu mutlu günümüzde sizleri de<br>aramizda görmekten mutluluk<br>duyacagiz.</p>

    <p class="invited">Davetlisiniz</p>

    <address class="venue">VELMORA<br>Kestanelik, Çınar Cad. No: 14<br>Yalıköy, Istanbul</address>

    <p class="event-date">24 Ağustos 2024</p>
  </section>

</main>
</body>
</html>
```